Business Card Design

We need the business card for our new business based in St. Marys, we manufacture mainly bubble wraps. And we would like the design to use our company logo and also make it easy for people to understand right away we are bubble wrap manufacturer

Industry/Entity Type

Business

Contact Information for Business Card

Cushora Pty Ltd, 14 Harlow Lane Elmvale NSW 2748, Tel: 02 9481 5726, Fax: 9481 5739, Dao Lin, General Manager, Mobile :0427 315 640, dao.lin@cushora.com.au, Website: cushora.com.au

```html
<!DOCTYPE html>
<html lang="en">
<head>
<meta charset="utf-8">
<title>Cushora Business Card</title>
<link rel="stylesheet" href="https://fonts.googleapis.com/css2?family=Montserrat:wght@400;600&family=Oswald:wght@400&display=swap">
<style>
  :root {
    --stage: #141414;
    --card-dark: #111111;
    --card-dark-edge: #262626;
    --card-light: #ffffff;
    --brand-red: #c9464c;
    --brand-red-deep: #b23a40;
    --ink: #4a4a4a;
    --ink-soft: #6d6d6d;
    --muted-grey: #8a8a8a;
    --bar-grey: #d4d4d4;
    --white: #ffffff;
  }
  * { margin: 0; padding: 0; box-sizing: border-box; }
  html, body {
    width: 1200px; height: 871px; overflow: hidden;
    background: var(--stage);
  }
  .stage {
    position: relative; width: 1200px; height: 871px;
    display: flex; align-items: center; justify-content: center; gap: 40px;
  }
  .card {
    position: relative; width: 540px; height: 340px;
    border-radius: 18px; overflow: hidden;
  }

  /* Back of card */
  .card-back {
    background: linear-gradient(135deg, var(--card-dark-edge), var(--card-dark) 60%);
  }
  .card-back .accent-top {
    position: absolute; top: 22px; left: 210px; width: 250px; height: 8px;
    background: var(--brand-red);
  }
  .card-back .accent-bottom {
    position: absolute; bottom: 26px; left: 250px; width: 260px; height: 8px;
    background: var(--brand-red);
  }
  .card-back .wordmark {
    position: absolute; top: 96px; left: 0; right: 0; text-align: center;
    font-family: 'Montserrat', sans-serif; font-weight: 600;
    font-size: 62px; letter-spacing: 4px; color: var(--white); line-height: 1;
  }
  .card-back .tagline {
    position: absolute; top: 176px; left: 0; right: 0; text-align: center;
    font-family: 'Montserrat', sans-serif; font-weight: 400;
    font-size: 15px; letter-spacing: 5px; color: var(--muted-grey);
  }
  .card-back .website {
    position: absolute; top: 226px; left: 0; right: 0; text-align: center;
    font-family: 'Montserrat', sans-serif; font-weight: 600;
    font-size: 17px; letter-spacing: 4px; color: var(--white);
    text-transform: uppercase;
  }

  /* Front of card */
  .card-front { background: var(--card-light); }
  .card-front .brand {
    position: absolute; top: 38px; right: 30px; text-align: right;
  }
  .card-front .wordmark {
    font-family: 'Montserrat', sans-serif; font-weight: 600;
    font-size: 42px; letter-spacing: 3px; color: var(--ink); line-height: 1;
  }
  .card-front .tagline {
    margin-top: 10px;
    font-family: 'Montserrat', sans-serif; font-weight: 400;
    font-size: 10.5px; letter-spacing: 3px; color: var(--ink-soft);
  }
  .card-front .frame { position: absolute; inset: 0; }
  .card-front .person {
    position: absolute; top: 126px; left: 18px; color: var(--white);
    font-family: 'Montserrat', sans-serif;
  }
  .card-front .person-name {
    font-weight: 600; font-size: 22px; letter-spacing: 2px;
    font-variant: small-caps; line-height: 28px;
  }
  .card-front .person-title {
    font-weight: 400; font-size: 14px; letter-spacing: 2px;
    font-variant: small-caps; line-height: 18px;
  }
  .card-front .contacts {
    position: absolute; top: 180px; left: 18px; list-style: none;
    font-family: 'Oswald', sans-serif; font-size: 15px; color: var(--ink);
  }
  .card-front .contacts li {
    display: flex; align-items: center; gap: 10px; height: 25px;
  }
  .card-front .contacts svg { width: 14px; height: 14px; flex: none; }
  .card-front .address { font-size: 16px; }
  .card-front .footer-bar {
    position: absolute; bottom: 8px; left: 0; right: 0; height: 12px;
    background: var(--bar-grey);
  }
  .card-front .footer-accent {
    position: absolute; bottom: 8px; left: 250px; width: 240px; height: 12px;
    background: var(--brand-red);
  }
</style>
</head>
<body>
<main class="stage">

  <section class="card card-back" aria-label="Card back">
    <div class="accent-top"></div>
    <div class="wordmark">CUSHORA</div>
    <div class="tagline">PROTECTIVE PACKAGING SOLUTIONS</div>
    <div class="website">cushora.com.au</div>
    <div class="accent-bottom"></div>
  </section>

  <section class="card card-front" aria-label="Card front">
    <svg class="frame" width="540" height="340" viewBox="0 0 540 340">
      <line x1="270" y1="127" x2="540" y2="118" stroke="var(--brand-red)" stroke-width="2"/>
      <polygon points="0,126 272,126 246,154 0,154" fill="var(--brand-red)"/>
      <polygon points="0,154 246,154 232,172 0,172" fill="var(--brand-red-deep)"/>
    </svg>

    <div class="brand">
      <div class="wordmark">CUSHORA</div>
      <div class="tagline">PROTECTIVE PACKAGING SOLUTIONS</div>
    </div>

    <div class="person">
      <div class="person-name">Dao Lin</div>
      <div class="person-title">General Manager</div>
    </div>

    <ul class="contacts">
      <li>
        <svg viewBox="0 0 14 14" aria-hidden="true"><rect x="3.5" y="1" width="7" height="12" rx="1.5" fill="none" stroke="var(--brand-red)" stroke-width="1.6"/><circle cx="7" cy="11" r="0.9" fill="var(--brand-red)"/></svg>
        <span>0427 315 640</span>
      </li>
      <li>
        <svg viewBox="0 0 14 14" aria-hidden="true"><rect x="1" y="3" width="12" height="8" fill="var(--brand-red)"/><polyline points="1,3 7,8 13,3" fill="none" stroke="var(--white)" stroke-width="1"/></svg>
        <span>dao.lin@cushora.com.au</span>
      </li>
      <li>
        <svg viewBox="0 0 14 14" aria-hidden="true"><path d="M7 13 C3 8 2.5 6.5 2.5 5 A4.5 4.5 0 0 1 11.5 5 C11.5 6.5 11 8 7 13 Z" fill="var(--brand-red)"/><circle cx="7" cy="5" r="1.6" fill="var(--white)"/></svg>
        <span class="address">Cushora Pty Ltd, 14 Harlow Lane Elmvale NSW 2748</span>
      </li>
      <li>
        <svg viewBox="0 0 14 14" aria-hidden="true"><path d="M1 5 Q7 1 13 5 L11 6.5 L9.5 5 L4.5 5 L3 6.5 Z" fill="var(--brand-red)"/><rect x="3" y="7" width="8" height="5" rx="1" fill="var(--brand-red)"/></svg>
        <span>02 9481 5726,</span>
      </li>
      <li>
        <svg viewBox="0 0 14 14" aria-hidden="true"><rect x="4" y="1.5" width="6" height="4" fill="none" stroke="var(--brand-red)" stroke-width="1.2"/><rect x="1" y="5.5" width="12" height="7" rx="1" fill="var(--brand-red)"/></svg>
        <span>9481 5739</span>
      </li>
    </ul>

    <div class="footer-bar"></div>
    <div class="footer-accent"></div>
  </section>

</main>
</body>
</html>
```